Harborline Kidney Services Brochure - Marketing brochure for a dialysis company in the USA

I want a brochure to be created for my business. I have a brochure that can be used as a comparison. My old Company name is Bluewater Renal Infusion Partners. The new Company Name is Harborline Kidney Services. I have a sample of the Old Brochure. and I uploaded the Logo of HKS. It will be used by my sales agents to introduce my company to potential client hospitals.

Target Market(s)

CEOs of Acute Hospitals and Medical Centers

Industry/Entity Type

Health Care

Requirements
Must have
• Use the sample as a guide. This project is for a 4 page brochure. (2 letter size pages folded in half crosswise) Use the text from the old brochure to the new brochure, replacing the old info with the new company info as needed.
Nice to have
• Here is my company info:
• Harborline Kidney Services
• 4180 W 61st Ave
• Suite D
• It will be nice if the designer can give me the project files that would allow me to edit the text of the brochure.
• McAllen, TX 78392
• (956) 417-2863
• admin@HarborlineKidneyLLC.example
• www.harborlinekidney.example

```html
<!DOCTYPE html>
<html lang="en">
<head>
<meta charset="utf-8">
<title>Harborline Kidney Services Brochure Spread</title>
<link href="https://fonts.googleapis.com/css2?family=Cabin:wght@400;500&display=swap" rel="stylesheet">
<style>
  :root {
    --backdrop: #b9b9b9;
    --paper: #ffffff;
    --navy: #124684;
    --sky: #1a9ddb;
    --slate: #6a6a6c;
    --ink: #2b2b2b;
    --muted: #8a8f99;
    --photo-light: #dfe3e8;
    --photo-cool: #b9cbd8;
    --pastel-pink: #eee2ea;
    --pastel-teal: #e0f0f0;
    --pastel-lilac: #e4e4ee;
  }
  * { box-sizing: border-box; margin: 0; padding: 0; }
  html, body { width: 1200px; height: 962px; overflow: hidden; }
  body {
    background: radial-gradient(ellipse at center, #d6d6d6 0%, var(--backdrop) 100%);
    font-family: "Cabin", sans-serif;
    position: relative;
  }
  .spread {
    position: absolute;
    left: 60px; top: 131px;
    width: 1080px; height: 700px;
    display: flex;
    box-shadow: 0 20px 40px rgba(0,0,0,.25);
  }
  .page { position: relative; width: 540px; height: 700px; background: var(--paper); overflow: hidden; }
  .page--left { border-right: 1px solid #e6e6e6; }

  .photo { position: absolute; }
  .photo--machine-top { left: 0; top: 0; width: 270px; height: 250px;
    background: linear-gradient(160deg, #ffffff 0%, var(--photo-light) 60%, #c9ced4 100%); }
  .photo--blood-sample { left: 270px; top: 330px; width: 270px; height: 190px;
    background: linear-gradient(135deg, #eef3f7 0%, var(--photo-cool) 60%, #8fa9bd 100%); }
  .photo--machine-bottom { left: 0; top: 460px; width: 270px; height: 190px;
    background: linear-gradient(180deg, #f4f6f8 0%, var(--photo-light) 100%); }
  .photo--infusion-pumps { left: 0; top: 400px; width: 480px; height: 250px;
    background: linear-gradient(120deg, #cfd8de 0%, #a9bcc6 45%, #7fa9a8 75%, #e3e8ec 100%); }

  .decoration-area {
    position: absolute; right: 0; top: 50px; width: 250px; height: 330px;
    background: linear-gradient(135deg, var(--pastel-pink) 0%, var(--pastel-teal) 55%, var(--pastel-lilac) 100%);
  }

  .panel { position: absolute; padding: 26px 24px; color: #fff; }
  .panel--navy { left: 270px; top: 90px; width: 270px; height: 240px; background: var(--navy); }
  .panel--sky { left: 0; top: 250px; width: 270px; height: 210px; background: var(--sky); }
  .panel--slate { left: 270px; top: 520px; width: 270px; height: 180px; background: var(--slate); }

  .section-title { font-weight: 500; font-size: 13px; letter-spacing: .06em; text-transform: uppercase; margin-bottom: 8px; }
  .panel--sky .section-title { text-align: center; }
  .body-copy { font-size: 10.5px; line-height: 1.35; margin-bottom: 10px; }

  .page-number {
    position: absolute; width: 28px; height: 28px;
    background: var(--sky); color: #fff;
    font-size: 12px; display: flex; align-items: center; justify-content: center;
  }
  .page--left .page-number { left: 180px; top: 662px; }
  .page--right .page-number { left: 256px; top: 662px; }

  .article { position: absolute; left: 40px; top: 80px; width: 230px; color: var(--ink); }
  .article .section-title { color: var(--muted); font-size: 11px; }
  .article .body-copy { font-size: 10px; }
</style>
</head>
<body>
  <main class="spread">
    <section class="page page--left">
      <div class="photo photo--machine-top" role="img" aria-label="Photo of a dialysis machine"></div>

      <div class="panel panel--navy">
        <h2 class="section-title">2. Small project name</h2>
        <p class="body-copy">Our acute dialysis team works at the bedside with hospital staff, giving steady treatment around the clock and clear reports after every session.</p>
        <p class="body-copy">Trained nurses bring mobile equipment to each unit, follow your protocols and keep downtime low so patients receive care when they need it most.</p>
      </div>

      <div class="panel panel--sky">
        <h2 class="section-title">Small project name</h2>
        <p class="body-copy">Trained nurses bring mobile equipment to each unit, follow your protocols and keep downtime low so patients receive care when they need it most.</p>
      </div>

      <div class="photo photo--blood-sample" role="img" aria-label="Photo of a gloved hand holding a blood sample tube"></div>
      <div class="photo photo--machine-bottom" role="img" aria-label="Photo of a bedside apheresis machine"></div>

      <div class="panel panel--slate">
        <h2 class="section-title">Small project name</h2>
        <p class="body-copy">Our acute dialysis team works at the bedside with hospital staff, giving steady treatment around the clock and clear reports after every session.</p>
      </div>

      <span class="page-number">3</span>
    </section>

    <section class="page page--right">
      <article class="article">
        <h2 class="section-title">2. Small project name</h2>
        <p class="body-copy">Our acute dialysis team works at the bedside with hospital staff, giving steady treatment around the clock and clear reports after every session.</p>
        <p class="body-copy">Trained nurses bring mobile equipment to each unit, follow your protocols and keep downtime low so patients receive care when they need it most.</p>
      </article>

      <div class="decoration-area" role="img" aria-label="Decorative pastel pattern area"></div>

      <div class="photo photo--infusion-pumps" role="img" aria-label="Photo of a nurse operating stacked infusion pumps"></div>

      <span class="page-number">2</span>
    </section>
  </main>
</body>
</html>
```